Emergency Medical Training and Events Company Business Needs Business Card Design

We are in need of a business card for our dynamic company expanding its customer base and need to be easily contacted and identified for when we visit with government officials, potential EMS / Fire agencies and county coordinators to arrange for training programs for first responders to better prepare them for critical thinking at critical incidents.

Target Market(s)

EMS/Fire and Event Promoters

Industry/Entity Type

Medical

Contact Information for Business Card

Two cards, comparable designs:

Martin K. Halvey, Principal, m.halvey@rvqtlo.com
Owen Tash, Event and Training Specialist, o.tash@rvqtlo.com

Font styles to use
Other font styles liked:
• Cambria

Colors

Designer to choose colors to be used in the design.

Requirements
Must have
• Company Logo, Spots for Name, Title, Phone Number, Email, Website
• A bullet list stating that we offer, QRB CPR and First Aid Instructors, Hold the Line Instructors, Event EMS, CME's, MCI Training and Planning. We prefer to have a black background for the card but if you can make a blue or white card stand out we would review that as well.
Should not have
• Tacky logos or special sayings ... simple, elegant, professional is the look we seek

```html
<!DOCTYPE html>
<html lang="en">
<head>
<meta charset="utf-8">
<title>Rovaq Training — Business Card</title>
<link href="https://fonts.googleapis.com/css2?family=Lato:wght@400;700;900&display=swap" rel="stylesheet">
<style>
  :root {
    --navy: #0f1f5c;
    --navy-deep: #0b1850;
    --red: #d0161e;
    --white: #ffffff;
    --ink: #141b3a;
    --stage: #2a2a2a;
  }
  * { box-sizing: border-box; margin: 0; padding: 0; }
  html, body { width: 1200px; height: 878px; overflow: hidden; }
  body {
    background: var(--stage);
    font-family: "Lato", sans-serif;
    display: flex;
    align-items: center;
    justify-content: center;
    gap: 40px;
  }
  .card {
    width: 540px;
    height: 309px;
    position: relative;
    overflow: hidden;
    box-shadow: 0 10px 30px rgba(0,0,0,.5);
  }

  .wordmark {
    font-weight: 900;
    font-size: 28px;
    line-height: 1;
    white-space: nowrap;
  }

  /* Back */
  .card-back { background: var(--navy-deep); color: var(--white); }
  .card-back .wordmark {
    position: absolute; top: 36px; right: 32px;
    color: var(--white);
  }
  .services {
    position: absolute; top: 112px; right: 32px;
    list-style: none;
    text-align: right;
    font-size: 15px;
    line-height: 23px;
  }
  .services li { display: flex; justify-content: flex-end; align-items: center; gap: 10px; }
  .services li::after {
    content: "";
    width: 0; height: 0;
    border-top: 5px solid transparent;
    border-bottom: 5px solid transparent;
    border-right: 9px solid var(--red);
  }

  /* Front */
  .card-front { background: var(--white); color: var(--ink); }
  .person { position: absolute; top: 30px; left: 38px; }
  .person-name { color: var(--red); font-weight: 900; font-size: 26px; line-height: 1.1; }
  .person-title { color: var(--navy); font-size: 15px; margin-top: 2px; }
  .front-brand {
    position: absolute; top: 118px; right: 32px;
    display: flex; align-items: center; gap: 12px;
  }
  .front-brand .mark {
    width: 44px; height: 44px; border-radius: 50%;
    background: var(--red);
    flex: none;
  }
  .front-brand .wordmark { color: var(--navy); }
  .contacts {
    position: absolute; top: 182px; left: 38px;
    list-style: none;
    font-size: 16px;
    line-height: 23px;
    color: var(--ink);
  }
  .contacts li { display: flex; align-items: center; gap: 10px; }
  .contacts svg { width: 13px; height: 13px; flex: none; }
  .icon-fill { fill: var(--red); }
  .icon-line { fill: none; stroke: var(--red); stroke-width: 2.4; stroke-linejoin: round; }
  .rule {
    position: absolute; left: 24px; right: 32px; top: 254px;
    height: 1px; background: var(--red); opacity: .7;
  }
  .address {
    position: absolute; top: 262px; left: 24px;
    display: flex; align-items: center; gap: 10px;
    font-size: 16px; color: var(--ink);
  }
  .address svg { width: 12px; height: 15px; fill: var(--red); }
  .footer-band {
    position: absolute; left: 0; right: 0; bottom: 0; height: 12px;
    background: var(--navy);
  }
  .footer-band::before {
    content: ""; position: absolute; left: 0; top: 0; bottom: 0; width: 46px;
    background: var(--red);
    border-right: 4px solid var(--white);
  }
</style>
</head>
<body>

  <section class="card card-back" aria-label="Card back">
    <div class="wordmark">Rovaq Training</div>
    <ul class="services">
      <li>QRB CPR</li>
      <li>First Aid Instructors</li>
      <li>Hold the Line Instructors</li>
      <li>Event EMS</li>
      <li>CME's</li>
      <li>MCI Training and Planning</li>
    </ul>
  </section>

  <section class="card card-front" aria-label="Card front">
    <div class="person">
      <h1 class="person-name">Martin K. Halvey</h1>
      <p class="person-title">Principal</p>
    </div>

    <div class="front-brand">
      <span class="mark"></span>
      <span class="wordmark">Rovaq Training</span>
    </div>

    <ul class="contacts">
      <li>
        <svg viewBox="0 0 24 24"><path class="icon-fill" d="M6.6 10.8a15 15 0 0 0 6.6 6.6l2.2-2.2a1 1 0 0 1 1-.25 11.4 11.4 0 0 0 3.6.57 1 1 0 0 1 1 1V20a1 1 0 0 1-1 1A17 17 0 0 1 3 4a1 1 0 0 1 1-1h3.5a1 1 0 0 1 1 1c0 1.25.2 2.45.57 3.57a1 1 0 0 1-.25 1z"/></svg>
        1234567890
      </li>
      <li>
        <svg viewBox="0 0 24 24"><path class="icon-line" d="M2 5h20v14H2z M2 5l10 8 10-8"/></svg>
        m.halvey@rvqtlo.com
      </li>
      <li>
        <svg viewBox="0 0 24 24"><circle class="icon-line" cx="12" cy="12" r="9.5"/><path class="icon-line" d="M2.5 12h19M12 2.5c3 3 3 16 0 19M12 2.5c-3 3-3 16 0 19"/></svg>
        www.rvqtlo.com
      </li>
    </ul>

    <div class="rule"></div>

    <div class="address">
      <svg viewBox="0 0 24 30"><path d="M12 0a11 11 0 0 0-11 11c0 8 11 19 11 19s11-11 11-19A11 11 0 0 0 12 0zm0 15a4 4 0 1 1 0-8 4 4 0 0 1 0 8z"/></svg>
      1234 First Line Address 5678 Second Line Address
    </div>

    <div class="footer-band"></div>
  </section>

</body>
</html>
```